Attractive Flyer for Moving Company

Our Company called "Harborlight Moving Company".
We provide moving service for home and businesses
We need a flyer for a moving company, located in San Diego, CA USA
Flyer size will be 7 x 5 inches, double sided.

Flyer needs to be very attractive and catchy for eye. I want people to keep it even if they dont need our service. I attached a lot of text in separate word file.
Logo, brief and additional pictures are attached.

Target Market(s)

27 years - 55 Years old

Industry/Entity Type

Moving Company

Colors
ec1f27
3176b5
ffffff

Requirements
Must have
• Attached in Word File
Nice to have
• Please be creative in placing a text and selecting a back ground picture.

```html
<!DOCTYPE html>
<html lang="en">
<head>
<meta charset="utf-8">
<title>Harborlight Moving Company – Flyer</title>
<link rel="stylesheet" href="https://fonts.googleapis.com/css2?family=Open+Sans:wght@400;600;700;800&display=swap">
<style>
  :root{
    --page:#e9e6dc;
    --white:#ffffff;
    --brand-red:#ec1f27;
    --brand-blue:#3176b5;
    --sky-top:#f3b444;
    --sky-mid:#d0621f;
    --ground:#2a0e06;
    --band:rgba(0,0,0,.72);
    --accent:#f7a52a;
    --pill:#e9a43a;
    --deal-ink:#4a1408;
    --deal-bg-top:#f6eeee;
    --deal-bg-bottom:#fbf7f4;
    --voucher:#3e1207;
  }
  *{box-sizing:border-box;margin:0;padding:0}
  html,body{width:1200px;height:1200px;overflow:hidden}
  body{background:var(--page);font-family:"Open Sans",Arial,sans-serif;position:relative}
  .flyer{position:absolute;left:261px;width:681px;height:488px;overflow:hidden;box-shadow:0 6px 14px rgba(0,0,0,.25)}
  .flyer--front{top:98px}
  .flyer--back{top:634px}

  /* front */
  .hero-photo{position:absolute;inset:0;background:
      radial-gradient(ellipse 55% 35% at 55% 18%,rgba(255,230,150,.85),transparent 70%),
      linear-gradient(180deg,var(--sky-top) 0%,var(--sky-mid) 38%,#6a2410 62%,var(--ground) 100%)}
  .headline{position:absolute;top:14px;width:100%;text-align:center;color:var(--white);font-size:56px;font-weight:600;text-shadow:0 3px 6px rgba(0,0,0,.45);letter-spacing:-.5px}
  .keep-band{position:absolute;top:212px;left:0;right:0;height:50px;background:var(--band);color:var(--white);text-align:center;font-size:15.5px;font-weight:600;line-height:22px;padding-top:3px}
  .services{position:absolute;left:20px;top:288px;color:var(--white);font-size:10.5px;font-weight:600;line-height:14px}
  .services h3{font-size:11px;font-weight:700}
  .services ul{list-style:none;padding-left:14px}
  .services .call{margin-top:8px}
  .services .contact{padding-left:14px;font-size:9.5px;line-height:12.5px}
  .reverse-pill{position:absolute;left:16px;top:452px;background:var(--pill);color:var(--ground);font-size:10.5px;font-weight:700;padding:4px 8px;border-radius:4px}
  .brand-box{position:absolute;background:var(--white);border-radius:6px;display:flex;align-items:center;justify-content:center;gap:8px;box-shadow:0 2px 5px rgba(0,0,0,.3)}
  .brand-box .dot{width:12px;height:12px;border-radius:50%;background:var(--brand-red);flex:none}
  .brand-name{color:var(--brand-blue);font-weight:800;text-align:center;line-height:1.1}
  .flyer--front .brand-box{left:256px;top:294px;width:158px;height:72px}
  .flyer--front .brand-name{font-size:14px}
  .credentials{position:absolute;left:226px;top:374px;width:218px;text-align:center;color:var(--white);font-size:9.5px;line-height:12px;font-weight:600}
  .credentials small{display:block;font-size:7.5px}
  .badges{position:absolute;left:284px;top:406px;display:flex;gap:18px}
  .badge-square{width:32px;height:44px;background:#2b5d8c;border-radius:3px}
  .badge-circle{width:42px;height:42px;border-radius:50%;background:#c4161c}
  .why{position:absolute;left:462px;top:288px;color:var(--white);font-size:10.3px;font-weight:600;line-height:13.5px}
  .why h3{color:var(--accent);font-size:14px;font-weight:700;margin-bottom:5px}
  .why ul{list-style:none}
  .why .sub{padding-left:8px}

  /* back */
  .deal-photo{position:absolute;inset:0;background:
      radial-gradient(ellipse 40% 30% at 72% 28%,rgba(200,150,150,.35),transparent 70%),
      linear-gradient(180deg,var(--deal-bg-top) 0%,#f1e3e1 45%,var(--deal-bg-bottom) 100%)}
  .flyer--back .brand-box{left:209px;top:52px;width:248px;height:110px}
  .flyer--back .brand-name{font-size:22px}
  .deal{position:absolute;top:200px;width:100%;text-align:center;color:var(--deal-ink)}
  .deal h2{font-size:21px;font-weight:600}
  .deal .terms{font-size:7.5px;font-weight:600;margin-top:6px}
  .deal .offers{font-size:14px;font-weight:700;line-height:21px;margin-top:14px}
  .deal .included{font-size:8.5px;font-weight:700;line-height:13px;margin-top:12px}
  .deal .included h4{font-size:8.5px;font-weight:700;margin-bottom:1px}
  .voucher{position:absolute;left:171px;top:440px;width:347px;height:36px;background:var(--voucher);color:var(--white);border-radius:4px;font-size:11px;font-weight:700;display:flex;align-items:center;justify-content:center}
</style>
</head>
<body>

<section class="flyer flyer--front">
  <div class="hero-photo" role="img" aria-label="Sunset over a mountain range with a silhouetted person leaping between rocky peaks"></div>
  <h1 class="headline">“Need MOVERS?”</h1>
  <p class="keep-band">Not moving soon? Keep this flyer for later and/or share it with friends.<br>Promotion is valid until January 1st, 2019)</p>

  <div class="services">
    <h3>MOVING SERVICE:</h3>
    <ul>
      <li>Residential, Long Distance,</li>
      <li>Commercial,</li>
      <li>Loading / Unloading rental truck</li>
      <li>&nbsp;/ portable storage,</li>
      <li>Packing Service</li>
    </ul>
    <h3 class="call">CALL FOR A QUICK ESTIMATE</h3>
    <p class="contact">Toll Free: 1-855-555-0142<br>Or Request Your Estimate online<br>www.HarborlightMoving.com</p>
  </div>
  <div class="reverse-pill">See reverse side for promotional offers</div>

  <div class="brand-box"><span class="dot"></span><span class="brand-name">Harborlight<br>Moving Company</span></div>
  <div class="credentials">Licensed &amp; Fully Insured<small>CAL PUC #104872 US DOT #3390512</small></div>
  <div class="badges"><span class="badge-square"></span><span class="badge-circle"></span></div>

  <div class="why">
    <h3>Why Call Us?</h3>
    <ul>
      <li>- Customer Oriented Service</li>
      <li>- Years of Great reputation</li>
      <li class="sub">(Lots of 5 Star Reviews)</li>
      <li>- Affordable pricing</li>
      <li>- Professional, efficient, strong movers</li>
      <li>- We always handle your belongings</li>
      <li class="sub">with care</li>
      <li>- Clean and equipped trucks</li>
      <li>- Absolutely NO surprising fees</li>
    </ul>
  </div>
</section>

<section class="flyer flyer--back">
  <div class="deal-photo" role="img" aria-label="Faded mountain landscape with a leaping figure, washed out behind the offer"></div>
  <div class="brand-box"><span class="dot"></span><span class="brand-name">Harborlight<br>Moving Company</span></div>
  <div class="deal">
    <h2>Your Special Deal</h2>
    <p class="terms">(Cannot be used with any other promotions or coupons)</p>
    <p class="offers">SAVE 15% -25% on your move<br>$235 – 3 hours of Moving Service with 2 PRO MOVERS<br>$325 - 3 hours of Moving Service with 3 PRO MOVERS<br>+ 20% OFF for boxes and packing supplies.</p>
    <div class="included">
      <h4>INCLUDED IN PRICE</h4>
      <p>- Protection of your furniture with specialized blankets and plastic wrap.</p>
      <p>- Dis-assembly and reassembly of your furniture.</p>
      <p>- Wardrobe boxes for the duration of moving process.</p>
    </div>
  </div>
  <div class="voucher">Keep this voucher it is valid until January 1st 2019</div>
</section>

</body>
</html>
```